I need a cover designed for a leadership book to fit my brand of my podcast, Chat with Your Druggist, www.remedyguidance-hub.com, with blues and greens and a professional look since it will be for a professional audience of pharmacists.

Some ideas for an image for the cover might be a woman's hand holding a compass with a road, but I welcome other ideas.

Title of the book is
"Where Chemists Steer: Insights from Ladies [in Focus] Who Are Guiding, Thriving, and Shaping Dispensaries"

```html
<!DOCTYPE html>
<html lang="en">
<head>
<meta charset="utf-8">
<title>Where Chemists Steer – Book Cover</title>
<link rel="stylesheet" href="https://fonts.googleapis.com/css2?family=Bebas+Neue&family=Montserrat:wght@400;600;700;800&display=swap">
<style>
  :root {
    --page-bg: #ecebe8;
    --brand-blue: #3a6597;
    --brand-green: #5bb446;
    --sky-top: #f4f8fb;
    --sky-mid: #dbe9f2;
    --hills: #c9a865;
    --road: #5d6b78;
    --white: #ffffff;
  }
  * { box-sizing: border-box; margin: 0; padding: 0; }
  html, body {
    width: 1200px; height: 800px; overflow: hidden;
    background: var(--page-bg);
  }
  .canvas {
    position: relative; width: 1200px; height: 800px;
    display: flex; align-items: center; justify-content: center;
  }
  .cover {
    position: relative; width: 480px; height: 750px; overflow: hidden;
    box-shadow: 0 10px 30px rgba(0,0,0,0.18);
  }
  .cover-photo {
    position: absolute; inset: 0;
    background: linear-gradient(180deg,
      var(--sky-top) 0%, var(--sky-mid) 42%,
      #e4d7b4 52%, var(--hills) 62%,
      #8c8f88 72%, var(--road) 88%, #4f5c68 100%);
  }
  .tagline {
    position: absolute; top: 50px; left: 0; right: 0;
    text-align: center; font-family: "Montserrat", sans-serif;
    font-weight: 700; font-size: 13.5px; letter-spacing: 0.06em;
    line-height: 1.55; color: var(--brand-blue);
  }
  .tagline .accent { color: var(--brand-green); font-weight: 800; }
  .title-kicker {
    position: absolute; top: 112px; left: 40px; right: 40px;
    display: flex; align-items: center; gap: 18px;
  }
  .title-kicker .rule { flex: 1; height: 2px; background: var(--brand-blue); }
  .title-kicker .word {
    font-family: "Bebas Neue", sans-serif; font-size: 54px;
    color: var(--brand-blue); letter-spacing: 0.04em; line-height: 1;
  }
  .title-main {
    position: absolute; top: 170px; left: 0; right: 0; text-align: center;
    font-family: "Bebas Neue", sans-serif; font-size: 118px; line-height: 0.95;
    color: var(--brand-green); letter-spacing: 0.02em;
  }
  .title-hero {
    position: absolute; top: 282px; left: 0; right: 0; text-align: center;
    font-family: "Bebas Neue", sans-serif; font-size: 226px; line-height: 1;
    color: var(--brand-blue); letter-spacing: 0; white-space: nowrap;
  }
  .author-band {
    position: absolute; left: 0; right: 0; bottom: 0; height: 62px;
    background: var(--brand-green); display: flex; align-items: center; justify-content: center;
    font-family: "Montserrat", sans-serif; color: var(--white);
    font-size: 21px; letter-spacing: 0.04em;
  }
  .author-band .name { font-weight: 800; text-transform: uppercase; }
  .author-band .credentials { font-weight: 400; }
</style>
</head>
<body>
  <main class="canvas">
    <section class="cover">
      <div class="cover-photo" role="img" aria-label="Photo of a hand holding a compass on an open road stretching through golden hills under a pale sky"></div>
      <p class="tagline">
        <span class="accent">INSIGHTS FROM LADIES</span> (IN FOCUS) WHO ARE<br>
        GUIDING, THRIVING, AND SHAPING DISPENSARIES
      </p>
      <div class="title-kicker">
        <span class="rule"></span>
        <span class="word">WHERE</span>
        <span class="rule"></span>
      </div>
      <h1 class="title-main">CHEMISTS</h1>
      <p class="title-hero">STEER</p>
      <footer class="author-band">
        <span class="name">Marlene Ashworth</span><span class="credentials">,&nbsp;PharmD, MBA</span>
      </footer>
    </section>
  </main>
</body>
</html>
```